4D Hush Little Nest Luxury Ultrasound Billboard

Design a HIGH-END, MODERN billboard for my private prenatal ultrasound studio, 4D Hush Little Nest, located in Pace, Florida.
This billboard will be viewed by drivers traveling at highway speeds, so it must be extremely clean, simple, and readable within 6 seconds.
About My Business
4D Hush Little Nest is a private prenatal ultrasound studio specializing in:
Highest technology 4D/HD Ultrasounds
Early Gender Determination
Pregnancy Confirmation
I have been serving families for nearly 10 years and is known for creating a memorable experience, not just an ultrasound appointment.
Design Style
I DO NOT want:
Flowers
Leaves
Swirls
Glitter
Hearts everywhere
Busy backgrounds
Generic maternity stock graphics
I DO want:
Modern
Luxury
Upscale
Clean
Professional
Eye-catching
Premium medical spa feel
Colors
Use colors from my logo:
LOGO Green ( or a deep green)
Black
White
Soft Gold accents
Images:
Incorporate my professional headshot in a clean, modern way, logo, and the ultrasound images
Text
Keep wording minimal.
Primary Headline ( OPEN TO IDEAS) :
EXAMPLES ( WOULD RATHER SOMETHING MORE CATCHY)
" ADVANCED IMAGING. UNFORGETTABLE MOMENTS"
"MEET YOUR BABY BEFORE BIRTH"
Under headline:
4D Ultrasound • Early Gender • Pregnancy Confirmation
Business Name:
4D Hush Little Nest
Private Prenatal Ultrasound Studio
Phone Number:
850-471-3905
Important
This billboard must be readable in 5–6 seconds from a moving vehicle.
Less text is better.
The phone number and business name must be visible from a distance.
The design should feel like a premium brand that immediately tells expecting parents:
“This is where I go to see my baby.”
Files Provided
Official logo
Headshot
Ultrasound images
Don’t make this look like a medical office billboard.
Make it look like a luxury baby experience billboard. That’s what separates 4D Hush Little Nest from hospitals, OB offices, and all the new studios popping up around you. The emotional connection is what gets moms to book. ❤️
Billboard Size - 10.6” x 36”

```html
<!DOCTYPE html>
<html lang="en">
<head>
<meta charset="utf-8">
<title>4D Hush Little Nest Billboard</title>
<link href="https://fonts.googleapis.com/css2?family=Poppins:wght@500;600;700&family=Playfair+Display:wght@700&display=swap" rel="stylesheet">
<style>
  :root {
    --page-bg: #d2d2d2;
    --deep-green: #2b332d;
    --band-green: #56695b;
    --white: #ffffff;
    --ink: #262b27;
    --gold: #e3b552;
    --gold-light: #f3d48a;
    --gold-dark: #b98a2e;
    --logo-green: #4b5d50;
  }
  * { margin: 0; padding: 0; box-sizing: border-box; }
  html, body { width: 1105px; height: 1200px; overflow: hidden; }
  body { background: var(--page-bg); font-family: "Poppins", sans-serif; position: relative; }

  .billboard {
    position: absolute; left: 40px; top: 344px;
    width: 1025px; height: 512px;
    background: var(--white); overflow: hidden;
  }
  .hero-panel { position: absolute; left: 0; top: 0; width: 750px; height: 327px; background: var(--deep-green); }
  .service-band { position: absolute; left: 0; top: 327px; width: 760px; height: 103px; background: var(--band-green); }
  .gold-rule { position: absolute; left: 744px; top: 0; width: 6px; height: 226px;
    background: linear-gradient(180deg, var(--gold-light), var(--gold-dark)); }
  .headshot {
    position: absolute; left: 750px; top: 0; width: 275px; height: 430px;
    background: linear-gradient(135deg, #ecebe8 0%, #dcdad6 45%, #5b6b55 80%, #3f4c3f 100%);
  }
  .ultrasound-photo {
    position: absolute; left: 22px; top: 325px; width: 180px; height: 184px;
    border: 2px solid var(--white);
    background: radial-gradient(circle at 50% 50%, #b06a55 0%, #8a4a3a 55%, #3a1a14 100%);
  }

  .brand-box {
    position: absolute; left: 306px; top: 22px; width: 152px; height: 85px;
    background: var(--white); text-align: center; padding-top: 11px;
  }
  .brand-name { font-weight: 600; font-size: 17px; line-height: 20px; color: var(--logo-green); }
  .brand-tagline { font-weight: 500; font-size: 6.5px; letter-spacing: 0.3px; color: var(--logo-green); margin-top: 6px; white-space: nowrap; }

  .headline { position: absolute; left: 0; width: 744px; text-align: center; white-space: nowrap; }
  .headline-top { top: 126px; font-weight: 700; font-size: 55px; line-height: 60px; color: var(--white); letter-spacing: 0.5px; }
  .headline-gold {
    font-family: "Playfair Display", serif; font-weight: 700; font-size: 66px; line-height: 60px; letter-spacing: 1px;
    background: linear-gradient(180deg, var(--gold-light) 0%, var(--gold) 45%, var(--gold-dark) 100%);
    -webkit-background-clip: text; background-clip: text; color: transparent;
  }
  .headline-line2 { top: 184px; }
  .headline-line3 { top: 243px; }

  .service { position: absolute; font-weight: 600; font-size: 18px; line-height: 21px; color: var(--white); letter-spacing: 0.4px; white-space: nowrap; }
  .service-icon { position: absolute; }
  .service-divider { position: absolute; left: 463px; top: 334px; width: 1px; height: 80px; background: var(--white); opacity: 0.8; }

  .phone { position: absolute; left: 205px; top: 438px; width: 510px; text-align: center; white-space: nowrap;
    font-weight: 700; font-size: 62px; line-height: 70px; color: var(--ink); letter-spacing: 0.5px; }
  .footer-divider { position: absolute; left: 722px; top: 446px; width: 1px; height: 50px; background: #b5b5b5; }
  .tenure-label { position: absolute; left: 766px; top: 440px; font-weight: 600; font-size: 13.5px; color: var(--ink); white-space: nowrap; }
  .tenure-years { position: absolute; left: 764px; top: 454px; font-weight: 700; font-size: 44px; line-height: 50px; color: var(--gold); white-space: nowrap; }
</style>
</head>
<body>
  <main class="billboard">
    <div class="hero-panel"></div>
    <div class="service-band"></div>
    <div class="headshot" role="img" aria-label="Professional headshot of the studio owner seated beside an ultrasound machine"></div>
    <div class="gold-rule"></div>
    <div class="ultrasound-photo" role="img" aria-label="4D ultrasound image of twins face to face"></div>

    <div class="brand-box">
      <div class="brand-name">4D Hush<br>Little Nest</div>
      <div class="brand-tagline">PRENATAL ULTRASOUND STUDIO</div>
    </div>

    <h1 class="headline headline-top">ADVANCED IMAGING</h1>
    <div class="headline headline-gold headline-line2">UNFORGETTABLE</div>
    <div class="headline headline-gold headline-line3">MOMENTS</div>

    <svg class="service-icon" style="left:226px;top:344px" width="22" height="28" viewBox="0 0 22 28" fill="none" stroke="#fff" stroke-width="1.4" stroke-linecap="round">
      <path d="M4 6a10 10 0 0 1 14 0M6.5 9a6 6 0 0 1 9 0"/>
      <path d="M7 12h8l-1 8a3 3 0 0 1-6 0z"/>
      <path d="M11 23v4"/>
    </svg>
    <div class="service" style="left:271px;top:348px">4D ULTRASOUND</div>

    <svg class="service-icon" style="left:226px;top:383px" width="26" height="26" viewBox="0 0 26 26" fill="none" stroke="#fff" stroke-width="1.5" stroke-linecap="round">
      <circle cx="9" cy="11" r="5.5"/>
      <circle cx="14" cy="9" r="5.5"/>
      <path d="M9 16.5v7M6 21h6M18 5l5-4M19 1h4v4"/>
    </svg>
    <div class="service" style="left:273px;top:389px">EARLY GENDER</div>

    <div class="service-divider"></div>

    <svg class="service-icon" style="left:498px;top:349px" width="20" height="16" viewBox="0 0 20 16" fill="none" stroke="#fff" stroke-width="3" stroke-linecap="round" stroke-linejoin="round">
      <path d="M2 8l5 5L18 2"/>
    </svg>
    <div class="service" style="left:528px;top:346px">PREGNANCY<br>CONFIRMATION</div>

    <div class="phone">850-471-3905</div>
    <div class="footer-divider"></div>
    <div class="tenure-label">SERVING FAMILIES FOR NEARLY</div>
    <div class="tenure-years">10 YEARS</div>
  </main>
</body>
</html>
```